Commercial photographer, UAV drone photography & 360 walk-through visuals

I need a business card design that is minimalist but yet pretentiously creative. My target market are architects, designers, advertising agents and marketing managers. It is important to stress that though I am asking for a minimalist design it needs to have creative impact.

Target Market(s)

Architects, interiors designers, web-designers, artists

Contact Information for Business Card

Include my name, mobile [cell] number, email, web page and the company logo. Do not to include a postal address.

Colors

Designer to choose colors to be used in the design.

Requirements
Must have
• The following information is to be included:
• Milo Fenwick
• Photographer
• m: 07812 593174
• e: milo@mfimagery.co.uk
• w: mfimagery.co.uk

```html
<!DOCTYPE html>
<html lang="en">
<head>
<meta charset="utf-8">
<title>MF Imagery – Business Card</title>
<link rel="stylesheet" href="https://fonts.googleapis.com/css2?family=Open+Sans:wght@400;600;700&display=swap">
<style>
  :root {
    --backdrop: #a8acab;
    --card: #efefec;
    --ink: #1b1b1b;
    --ink-soft: #3a3a3a;
    --muted: #8d8d8d;
  }
  * { margin: 0; padding: 0; box-sizing: border-box; }
  html, body {
    width: 1200px; height: 824px; overflow: hidden;
    background: var(--backdrop);
    font-family: "Open Sans", Arial, sans-serif;
    color: var(--ink);
  }
  .stage {
    position: relative; width: 1200px; height: 824px;
    display: flex; align-items: center; justify-content: center; gap: 60px;
  }
  .card {
    position: relative; width: 480px; height: 274px;
    background: var(--card);
    box-shadow: 0 6px 18px rgba(0,0,0,.18);
  }
  /* front side */
  .card-front .marker {
    position: absolute; left: 0; top: 40px;
    width: 14px; height: 14px; background: var(--ink);
  }
  .identity { position: absolute; left: 32px; top: 34px; }
  .identity .name {
    font-size: 17px; font-weight: 700; letter-spacing: .5px;
    text-transform: uppercase; line-height: 1.2;
  }
  .identity .role {
    font-size: 12px; font-weight: 400; color: var(--muted);
    text-transform: uppercase; letter-spacing: .5px;
  }
  .contacts {
    position: absolute; left: 32px; top: 92px;
    list-style: none; font-size: 12.5px; color: var(--ink-soft);
  }
  .contacts li { display: flex; align-items: center; gap: 8px; line-height: 1.6; }
  .contacts svg { width: 11px; height: 11px; fill: var(--ink); flex: none; }
  .front-brand {
    position: absolute; right: 34px; bottom: 34px;
    font-size: 40px; font-weight: 600; letter-spacing: 1px;
    text-transform: uppercase; line-height: 1; color: var(--ink);
  }
  /* back side */
  .card-back {
    display: flex; align-items: center; justify-content: center;
  }
  .back-brand {
    font-size: 30px; font-weight: 600; letter-spacing: 6px;
    text-transform: uppercase; color: var(--ink);
  }
</style>
</head>
<body>
<main class="stage">
  <section class="card card-front" aria-label="Card front">
    <span class="marker"></span>
    <div class="identity">
      <p class="name">Milo Fenwick</p>
      <p class="role">Photographer</p>
    </div>
    <ul class="contacts">
      <li>
        <svg viewBox="0 0 12 12" aria-hidden="true"><path d="M2.5 1h2l1 3-1.3 1a6 6 0 0 0 2.8 2.8L8 6.5l3 1v2c0 .8-.7 1.5-1.5 1.5A8.5 8.5 0 0 1 1 2.5C1 1.7 1.7 1 2.5 1z"/></svg>
        <span>07812 593174</span>
      </li>
      <li>
        <svg viewBox="0 0 12 12" aria-hidden="true"><path d="M0 2h12v1L6 7 0 3z"/><path d="M0 4.2 6 8.2l6-4V10H0z"/></svg>
        <span>milo@mfimagery.co.uk</span>
      </li>
      <li>
        <svg viewBox="0 0 12 12" aria-hidden="true"><circle cx="6" cy="6" r="6"/></svg>
        <span>mfimagery.co.uk</span>
      </li>
    </ul>
    <p class="front-brand">MF Imagery</p>
  </section>

  <section class="card card-back" aria-label="Card back">
    <p class="back-brand">MF Imagery</p>
  </section>
</main>
</body>
</html>
```